A Hair, Beauty and Nails Wholesalers Needs a Business Card Design

We need a business card design for our company which is being passed from parents to daughter, so we wont to re-launch the company with an updated, modern, sophisticated, elegant, chic and fresh look which still incorporates the original colour scheme of Hot Pink, Dark Grey and White. The original logo which is attached can be used on the card but we would like to see some designs with the logo and some without, as we have not yet decided if we want the logo on the card. The name of our company is 'RM's Distributors' and the name of our website is RM's GlowandPolish.example.au. We specialise in supplying a massive range of Hair, Beauty and Nail products to the industry. We are based in QLD, Australia but ship many orders via our website all across Australia.

Industry/Entity Type

Business

```html
<!DOCTYPE html>
<html lang="en">
<head>
<meta charset="utf-8">
<title>RM's Distributors – Business Card</title>
<link rel="stylesheet" href="https://fonts.googleapis.com/css2?family=Great+Vibes&family=Didact+Gothic&display=swap">
<style>
  :root {
    --hot-pink: #e3168c;
    --dark-grey: #3d4043;
    --silver: #a7abaf;
    --silver-light: #e4e6e8;
    --white: #ffffff;
    --backdrop: #c9d0cf;
    --card-w: 540px;
    --card-h: 309px;
  }
  * { box-sizing: border-box; margin: 0; padding: 0; }
  html, body { width: 1200px; height: 900px; overflow: hidden; }
  body {
    background: var(--backdrop);
    display: flex;
    align-items: center;
    justify-content: center;
    gap: 40px;
    font-family: "Didact Gothic", "Century Gothic", sans-serif;
  }
  .card {
    position: relative;
    width: var(--card-w);
    height: var(--card-h);
    background: var(--white);
    overflow: hidden;
    box-shadow: 0 6px 18px rgba(0,0,0,.18);
  }

  /* Front */
  .front .pink-band {
    position: absolute; left: 0; right: 0; bottom: 0; height: 118px;
    background: var(--hot-pink);
  }
  .front .silver-rule {
    position: absolute; left: 0; right: 0; bottom: 118px; height: 14px;
    background: linear-gradient(180deg, var(--silver-light), var(--silver) 70%, var(--dark-grey));
  }
  .holder-name {
    position: absolute; left: 28px; top: 34px;
    font-family: "Great Vibes", cursive;
    font-size: 58px; color: var(--silver); line-height: 1;
  }
  .holder-title {
    position: absolute; left: 262px; top: 104px;
    font-size: 15px; letter-spacing: .5px; color: var(--dark-grey);
  }
  .contact {
    position: absolute; left: 28px; bottom: 16px;
    list-style: none; color: var(--white);
    font-size: 14px; line-height: 1.55; letter-spacing: .3px;
  }
  .brand {
    position: absolute; display: flex; align-items: center; gap: 8px;
    color: var(--hot-pink); font-weight: 400; white-space: nowrap;
  }
  .brand-dot { border-radius: 50%; background: var(--hot-pink); flex: none; }
  .front .brand { right: 24px; top: 140px; font-size: 16px; }
  .front .brand-dot { width: 14px; height: 14px; }

  /* Back */
  .back .pink-stripe {
    position: absolute; left: 0; right: 0; top: 46px; height: 10px;
    background: var(--hot-pink);
  }
  .back .silver-stripe {
    position: absolute; left: 0; right: 0; top: 62px; height: 8px;
    background: linear-gradient(180deg, var(--silver-light), var(--silver) 70%, var(--dark-grey));
  }
  .back .brand {
    left: 0; right: 0; top: 150px; justify-content: center;
    font-size: 40px; gap: 16px;
  }
  .back .brand-dot { width: 34px; height: 34px; }
</style>
</head>
<body>

  <section class="card front" aria-label="Business card front">
    <div class="silver-rule"></div>
    <div class="pink-band"></div>
    <h1 class="holder-name">Danielle Hartmann</h1>
    <p class="holder-title">Manager</p>
    <div class="brand"><span class="brand-dot"></span>RM's Distributors</div>
    <ul class="contact">
      <li>Ph: (07) 4555 0192</li>
      <li>27 Wattle Lane</li>
      <li>TOOWOOMBA, QLD 4350</li>
      <li>www.glowandpolish.example.au</li>
    </ul>
  </section>

  <section class="card back" aria-label="Business card back">
    <div class="pink-stripe"></div>
    <div class="silver-stripe"></div>
    <div class="brand"><span class="brand-dot"></span>RM's Distributors</div>
  </section>

</body>
</html>
```